Booklet for meditation CD to match existing CD cover

We need a design for a booklet that matches the meditation CD cover previously designed. It should look like it belongs to the CD as it will be inserted into the cover slot. I hope you can re-use some of the existing artwork. It should incorporate the logo and the text and probably the list of tracks as well. I have attached the original CD cover file, the logo file, photo file and the specs from the CD production company for the 8 page booklet. The spec also includes a cover spec. You can ignore that part. Please put all the text from the CD cover, as well as the track names and the credits from the CD cover into the booklet and the text describing the meditation in full which I have enclosed as a word file.

Target Market(s)

People interested in meditation and personal growth

Font styles to use
Serif

Colors
0555a3
876aae
a54499
e667a6
ee363c

Requirements
Must have
• must match the existing CD cover, must include logo and photo and text from CD cover
• Design, Fonts and colours should match CD cover.

```html
<!DOCTYPE html>
<html lang="en">
<head>
<meta charset="utf-8">
<title>The Current of Presence Meditation – Booklet Spreads</title>
<link href="https://fonts.googleapis.com/css2?family=Cinzel:wght@400;600&family=Roboto+Condensed:ital,wght@0,300;0,400;0,700;1,400&display=swap" rel="stylesheet">
<style>
  :root{
    --canvas:#e9e6e2;
    --label:#1c1c1c;
    --violet:#876aae;
    --magenta:#a54499;
    --heading:#1f3f8a;
    --body:#2b2f55;
    --white:#ffffff;
    --tagline:#f6e6f2;
    --page-bg:linear-gradient(180deg,#464a84 0%,#6f72ad 20%,#aca0cc 42%,#e2c3da 64%,#f2b8d1 84%,#ee9cc3 100%);
    --cover-bg:linear-gradient(180deg,#3b3f73 0%,#6f6b9e 30%,#b48fb8 60%,#c86fa6 85%,#7a3f78 100%);
  }
  *{box-sizing:border-box;margin:0;padding:0}
  html,body{width:1200px;height:1200px;overflow:hidden}
  body{background:var(--canvas);font-family:"Roboto Condensed",sans-serif;position:relative;color:var(--body)}

  .page-label{position:absolute;font-family:"Roboto Condensed",sans-serif;font-weight:300;font-size:35px;line-height:1.1;color:var(--label)}
  .page-label.left{text-align:right;right:918px}
  .page-label.right{left:913px}

  .spread{position:absolute;left:322px;width:556px;height:275px;display:flex;box-shadow:0 2px 6px rgba(0,0,0,.18)}
  .page{width:278px;height:100%;position:relative;overflow:hidden;background:var(--page-bg)}
  .page::after{content:"";position:absolute;inset:0;pointer-events:none;
    background:radial-gradient(ellipse at 50% 108%,rgba(255,255,255,.45),rgba(255,255,255,0) 55%)}

  .cols{position:absolute;top:22px;bottom:8px;left:23px;right:26px;display:grid;grid-template-columns:1fr 1fr;column-gap:11px;z-index:1}
  .col{overflow:hidden}
  .stage-title{font-family:"Cinzel",serif;font-weight:600;color:var(--heading);font-size:10px;line-height:1.05;margin:5px 0 2px}
  .stage-title:first-child{margin-top:0}
  p{font-size:5.4px;line-height:7px;color:var(--body);margin-bottom:2px}

  /* front cover */
  .front-cover{background:var(--cover-bg)}
  .cover-title{position:absolute;top:36px;left:0;right:0;text-align:center;font-family:"Cinzel",serif;font-weight:400;color:var(--white);font-size:24px;line-height:28px;z-index:2;text-shadow:0 1px 3px rgba(40,30,80,.4)}
  .tagline{position:absolute;font-family:"Cinzel",serif;color:var(--tagline);font-size:10px;line-height:12px;text-align:center;z-index:2;width:78px}
  .tagline.left{left:7px;top:97px}
  .tagline.right{right:9px;top:97px}
  .cover-art{position:absolute;left:40px;top:90px;width:200px;height:185px;z-index:1;
    background:radial-gradient(ellipse at 50% 30%,#6b3d52 0%,#8d5a78 25%,rgba(170,120,170,.3) 50%,rgba(0,0,0,0) 70%),
               radial-gradient(ellipse at 50% 115%,#5a2a66 0%,#b0548f 35%,rgba(0,0,0,0) 62%)}

  .brand{position:absolute;z-index:3;top:218px;width:98px;height:33px;background:var(--white);display:flex;align-items:center;justify-content:center;gap:5px}
  .brand .dot{width:8px;height:8px;border-radius:50%;background:var(--violet)}
  .brand .name{font-family:"Roboto Condensed",sans-serif;font-size:15px;color:var(--violet)}
  .brand.front{right:0;border-radius:17px 0 0 17px}
  .brand.back{left:0;border-radius:0 17px 17px 0}

  /* back cover */
  .portrait{position:absolute;left:23px;top:22px;width:62px;height:74px;z-index:2;border:1.5px solid var(--white);
    background:linear-gradient(160deg,#e8d6d0,#c7524a 45%,#5a2a3a)}
  .back-heading{position:absolute;left:23px;top:104px;font-family:"Cinzel",serif;font-weight:400;color:var(--white);font-size:12px;z-index:2}
  .back-body{position:absolute;left:23px;top:118px;width:104px;z-index:2}
  .back-body p{color:var(--white);font-size:5.2px;line-height:6.9px}
  .tracks{position:absolute;left:146px;top:20px;width:125px;z-index:2;color:var(--white)}
  .tracks h2{font-family:"Cinzel",serif;font-weight:400;font-size:11px;margin-bottom:10px}
  .tracks ol{list-style:none;font-size:5.6px;line-height:9.3px;font-style:italic}
  .more-info{position:absolute;right:28px;top:222px;width:130px;text-align:right;font-size:5.2px;line-height:9px;font-weight:700;color:var(--magenta);z-index:2}

  /* page 2 */
  .intro{position:absolute;top:22px;left:18px;right:18px;text-align:center;z-index:2}
  .intro h1{font-family:"Cinzel",serif;font-weight:400;color:var(--white);font-size:16px;line-height:16px;margin-bottom:10px}
  .intro p{font-size:5.8px;font-weight:700;color:var(--heading);line-height:9.6px;margin-bottom:3px}
  .intro h2{font-family:"Cinzel",serif;font-weight:400;color:var(--white);font-size:12px;margin:8px 0 9px}
  .stage-list{list-style:none;text-align:left;font-size:5.6px;font-weight:700;color:var(--heading);line-height:7.5px;padding-left:34px}
  .stage-list li{margin-bottom:4.5px}
  .figure{position:absolute;left:105px;top:135px;width:80px;height:110px;z-index:1;border-radius:40% 40% 20% 20%;
    background:radial-gradient(ellipse at 50% 50%,rgba(150,90,110,.4),rgba(150,90,110,0) 70%)}
</style>
</head>
<body>

<div class="page-label left" style="top:28px">Page 8<br>(back cover)</div>
<div class="page-label right" style="top:28px">Page 1<br>(front cover)</div>
<div class="page-label left" style="top:336px">Page 2</div>
<div class="page-label right" style="top:336px">Page 3</div>
<div class="page-label left" style="top:612px">Page 4</div>
<div class="page-label right" style="top:612px">Page 5</div>
<div class="page-label left" style="top:908px">Page 6</div>
<div class="page-label right" style="top:908px">Page 7</div>

<section class="spread" style="top:20px">
  <article class="page back-cover">
    <div class="portrait" role="img" aria-label="Portrait photograph of the meditation teacher"></div>
    <h2 class="back-heading">BACKGROUND</h2>
    <div class="back-body">
      <p>We created this meditation mainly for use in our workshops as a morning practice, yet it works just as well at home. Pillows can help soften the sounds during the wild phase. Its purpose is to bring you into your body, linking you through movement with both your physical and emotional self, and then using that lively, awake connection to open into an experience of essence.</p>
    </div>
    <div class="tracks">
      <h2>TRACKS</h2>
      <ol>
        <li>1. Trembling</li><li>2. The Current of Your Wild Energy</li><li>3. Embracing Yourself</li>
        <li>4. Gathering the Energy</li><li>5. Root of Instinct</li><li>6. Sacral Centre</li>
        <li>7. Power Centre</li><li>8. Heart Centre</li><li>9. Throat Centre</li>
        <li>10. Seat of Intuition</li><li>11. Crown Centre</li><li>12. Stillness</li>
        <li>13. Receiving the Infinite</li><li>14. Stillness</li><li>15. Celebration of Presence</li>
      </ol>
    </div>
    <div class="brand back"><span class="dot"></span><span class="name">Mara Quill</span></div>
    <p class="more-info">If you want to find out more<br>about workshops with Mara Quill,<br>go to www.maraquill.com</p>
  </article>
  <article class="page front-cover">
    <h1 class="cover-title">THE CURRENT OF<br>PRESENCE</h1>
    <div class="tagline left">A MEDITATION TO OPEN TO THE WHOLE OF YOU<br><br>A MEDITATION TO RISE LIGHT IN YOUR LIFE</div>
    <div class="tagline right">A MEDITATION TO MEET YOUR ROOTS AND YOUR WINGS</div>
    <div class="cover-art" role="img" aria-label="Illustration of a tree with deep roots over a glowing planet, a seated meditating figure at its base"></div>
    <div class="brand front"><span class="dot"></span><span class="name">Mara Quill</span></div>
  </article>
</section>

<section class="spread" style="top:314px">
  <article class="page">
    <div class="figure" role="img" aria-label="Soft silhouette of a seated meditating figure"></div>
    <div class="intro">
      <h1>THE CURRENT OF PRESENCE<br>MEDITATION</h1>
      <p>For this meditation you'll need room to move freely, ideally with a mattress or soft surface for the second and third stages. Keep a pillow close for the second stage.</p>
      <p>The meditation unfolds in 7 stages, moving from activity towards stillness.</p>
      <h2>THE SEVEN STAGES ARE</h2>
      <ol class="stage-list">
        <li>1 Trembling (standing)</li>
        <li>2 Meeting your wild energy (on the floor or mattress)</li>
        <li>3 Embracing yourself in your aliveness (on the floor or mattress)</li>
        <li>4 Rising through each energy centre or chakra of the body (coming up to standing part-way)</li>
        <li>5 Standing and receiving the energy of the infinite</li>
        <li>6 Led back into seated meditation for 15 minutes</li>
        <li>7 Celebration and returning to your day</li>
      </ol>
    </div>
  </article>
  <article class="page">
    <div class="cols">
      <div class="col">
        <h3 class="stage-title">First Stage:<br>Trembling</h3>
        <p>Stand with your feet roughly the width of your hips, both soles resting firmly on the ground. Keep your knees soft and start to let your body bounce, letting the shaking begin in the knees so that everything above the pelvis can move without effort. Respect what your body can do. There is no need to shake hard; a light, easy movement is enough. Never force it. If something aches or you feel unsure about your body, soften the movement, or lie down and shake only your arms and legs, or simply rest and watch.</p>
        <p>Let the whole upper body stay loose, releasing any tension so that all of you can tremble freely and gently, even your head. Shake out every thought and every feeling. Gather your attention down into the body so it rests in sensation rather than in thinking. Let the belly, the shoulders and the jaw hang loose, the mouth slightly open. Let each breath be full and unhurried.</p>
        <p>In this stage, keep any sounds on the inside.</p>
      </div>
      <div class="col">
        <h3 class="stage-title">Second Stage:<br>Meeting Your<br>Wild Energy</h3>
        <p>Your wild side wakes more easily when you are low on the floor, free to roll, release and move without effort. In this stage let your body be as untamed, loose and unguarded as it wants to be. Begin by holding the pillow so your hands can grip it, squeeze it and dig into it. You might even bite into it. Let your hips join in. Drop every inner censor. Give your body permission to move in ways it normally never would, beyond its usual habits and patterns.</p>
        <p>Keep your eyes closed, opening them only to check that you won't bump into anything. If you can, let wild sounds come along with the wild movements; if noise would be a problem, send your voice into the pillow. This energy can have many flavours, sometimes several at once. It may be joyful, furious or sensual. Welcome whatever comes and let the body lead. Watch out for slipping into an old routine, such as replaying a past quarrel again and again. Be open to every energy in you, not only the familiar ones. Stay curious about what is alive in you today. Forget about</p>
      </div>
    </div>
  </article>
</section>

<section class="spread" style="top:610px">
  <article class="page">
    <div class="cols">
      <div class="col">
        <p>how it went the last time; let today be fresh and meet yourself as you are now. Allow yourself to enjoy this raw, unedited energy. Breathe deeply. Move fully. Let hands, jaw and pelvis carry you into your wildness.</p>
        <h3 class="stage-title">Third Stage:<br>Embracing Yourself</h3>
        <p>Now that your energy has had room to run wild, you will probably notice a strong current moving through you. Savour it. Sense your life force, whatever its shape, colour, rhythm or warmth, streaming inside you. Shift your attention to slow, deep breathing so you can feel yourself more clearly. Welcome and befriend everything you meet within. Move gently and tenderly, perhaps stroking your own skin as you breathe softly yet fully, as a way of saying a wholehearted yes to yourself. Delight in being alive. Relax and sink into the softness of your body, keeping it gently in motion.</p>
      </div>
      <div class="col">
        <h3 class="stage-title">Fourth Stage:<br>Rising Through<br>Each of the<br>Energy Centres<br>or Chakras in the<br>Body</h3>
        <p>Gathering: Start by drawing all your energy down to the base of the body. Picture bright white light flowing downward from your head, your fingertips and your feet, pooling at the base of your trunk, the first chakra. Use the breath the way you would fan a fire, feeding it air so that your inner flame comes alive. Imagine breathing right into the base of the trunk. You can steer the energy by picturing it travel through you, by feeling it and guiding it, or by brushing your hands along your body as though sweeping the energy down to its base.</p>
        <h3 class="stage-title">1st Chakra:<br>Instinct - Nature</h3>
        <p>Now rest your whole attention in the centre of instinct at the very base of the trunk. We are about to travel upward through the chakras, the energy centres of your</p>
      </div>
    </div>
  </article>
  <article class="page">
    <div class="cols">
      <div class="col">
        <p>body. Even if this feels new, let your attention settle in each centre in turn and imagine the breath flowing there. The centre of instinct lies at the base of the body. It carries a primal force, an energy that longs to become life and to keep on living. It is raw and untamed. Picture a lioness guarding her cubs. It is instinct in its pure form, without reflection or second thoughts, the first spark of life unfolding.</p>
        <h3 class="stage-title">2nd Chakra:<br>Sacral - Desire</h3>
        <p>From here we carry the energy up to the sacral centre. This is the home of your sexual nature, of desire, of reaching out for what you want and for pleasure. Breathing into the area of your sex helps you meet it. There is nothing you need to do with this energy; simply notice the life moving there and let it flow in its own way.</p>
        <h3 class="stage-title">3rd Chakra:<br>Navel - Power</h3>
        <p>Next we rise to the centre of power. In martial arts this area is sometimes called the hara. It lies just under the</p>
      </div>
      <div class="col">
        <p>navel. As you breathe into this place you can meet your own personal strength, the power to stand fully in who you are and to sense your force there. If you have been lying on the mattress or floor, come up to standing during this part. Feel your feet on the ground as you walk your human path.</p>
        <h3 class="stage-title">4th Chakra: Heart</h3>
        <p>The fourth centre is the heart. Bring your breath to your heart. Imagine and feel the wild energies of the lower centres rising into it, and your heart turning all that fiery, restless passion into a calm, warm radiance that fills and surrounds you, giving you a deep inner yes to yourself. Rest in that yes, the one the heart offers whenever you tune in and let it hold all of you. Sense how wide the heart is, how much it can carry and embrace. Notice that your heart is far larger than your hurts. As you connect with this warmth, feel an inner mother holding you, a presence of great kindness wrapping you in care. Soften into it and let yourself receive this tender energy.</p>
      </div>
    </div>
  </article>
</section>

<section class="spread" style="top:906px">
  <article class="page">
    <div class="cols">
      <div class="col">
        <h3 class="stage-title">5th Chakra: Throat</h3>
        <p>This deep inner yes now moves up into the throat, the centre where your own unique way of being finds expression. It says yes to your voice, to how you live and show yourself, so that you can offer your gifts to the world. Sense the freedom to live and share yourself without fear or self-editing, knowing you are enough. Trust that what you bring is yours alone to give and that life welcomes it.</p>
        <h3 class="stage-title">6th Chakra:<br>Third Eye -<br>Intuition</h3>
        <p>Then let this yes to your being rise into the centre of intuition, the point between the eyebrows. It is a doorway beyond the physical self, often felt as a quiet inner knowing or a touch of deeper wisdom.</p>
        <p>The more attention you give this point, listening deeply, the more will come to you. Don't be concerned if nothing seems to happen at first. It is a practice, and it may be a sense you have not used for some time. Step in with curiosity and openness.</p>
      </div>
      <div class="col">
        <h3 class="stage-title">7th Chakra: Crown</h3>
        <p>Whatever you discover, let the energy keep rising to the crown of your head or just above it. Let your attention widen beyond yourself into a link with spirit that some part of you has always known. Perhaps you have already tasted this ground of awareness beyond the physical world. Let yourself grow still, dissolving into it the way a raindrop merges with the sea. Enter oneness. Nothing to do, nothing to reach for. Simply be with whatever appears as your awareness opens.</p>
        <h3 class="stage-title">Fifth Stage:<br>Receiving the<br>Energy</h3>
        <p>Take in the energy of the infinite and stand inside that awareness, giving yourself the rich gift of total stillness, without moving at all, for two minutes.</p>
        <h3 class="stage-title">Sixth Stage</h3>
        <p>You are led back down, grounding all this energy into your physical body. The body is still awake from the earlier stages of the journey and still open to be nourished by the source of all life. Let</p>
      </div>
    </div>
  </article>
  <article class="page">
    <div class="cols">
      <div class="col">
        <p>this current feed and brighten your physical form, opening each centre as it passes: the third eye, the throat, the heart, the power centre, the sex and the root.</p>
        <p>Let spirit flow back into your being and on into the earth below your feet, sensing yourself as one strand in the endless flow of life. Feel your own nature rising to meet spirit in a single unbroken circle. Stay awake to everything moving in you and find your way down into sitting in stillness.</p>
        <h3 class="stage-title">Sitting in<br>Meditation for<br>15 Minutes</h3>
        <p>A note on sitting. To gain the most from any silent meditation, keep the spine upright, as though a fine thread lifts you from the crown of your head while the body stays at ease. Comfort matters more than twisting the body into a pose that won't let you relax. Ideally three points of your body touch the floor. If you can rest easily in the lotus posture, wonderful. If you can sit cross-legged</p>
      </div>
      <div class="col">
        <p>on a cushion with both knees on the floor, that also works well. If you balance on your sitting bones with nothing beneath you, you will probably end up slumping; then it is usually wiser to lean against a wall, sit on a chair or stand. An upright spine holds you between full relaxation and full alertness, ready to rise like a samurai.</p>
        <p>While you sit quietly listening to the life flowing within, it can help to rest your attention on the breath. Whenever you notice you are lost in a thought, just let it go and return to this moment.</p>
        <h3 class="stage-title">Seventh Stage -<br>Celebration and<br>Returning to<br>Your Day</h3>
        <p>At last, as the music carries you out of the meditation, let it invite you into the beauty of this moment, into a celebration of life and all it offers, and above all a celebration of your own wholeness, the whole of who you are, here, now, today. Carry it into your day.</p>
      </div>
    </div>
  </article>
</section>

</body>
</html>
```